PowerPoint Template Design for business consulting company in Silicon Valley

I need a PowerPoint template to use as the starting point for new presentations. I have a logo but now need design that supports this. I've attached a very descriptive PDF that explains exactly what I need. Here is a list of deliverables: 1. PowerPoint Template that I will use as the starter presentation for all new Lantern Quorix presentationsDesigns for the following slides: See picture below for examples of structure:2. Title slide with subtitle3. Section header4. Title and body5. Title and 2 columns6. Title and 3 columns7. One column text8. Editable timeline to show months, or steps for a process9. Bullet design for unordered list (can be graphic)10. Bullet design for ordered list11. Recommended fonts for each design: Title, subtitle, list, captionOPTIONAL: Possible graphic elements to be used for section title slide backgrounds or graphic elements:--Your team / my team / people on project--Goals for project / presentation--Editable Timeline--Speaking--Writing--Listening--People collaborating / helping each otherI am happy to accept proposals for developing these optional elements in a separate project.

Requirements
Must have
• Must be FLAT design.
• Not flashy or garish. Must be subtle.

```html
<!DOCTYPE html>
<html lang="en">
<head>
<meta charset="utf-8">
<title>Lantern Quorix – Title Slide</title>
<link href="https://fonts.googleapis.com/css2?family=Montserrat:wght@400;500&display=swap" rel="stylesheet">
<style>
  :root {
    --page: #ececec;
    --panel-grey: #e6e7e9;
    --inner-grey: #eeeff0;
    --ring-white: #ffffff;
    --brand-blue: #26419a;
    --brand-green: #159a4f;
    --green-top: #1aa552;
    --green-bottom: #0f8f49;
    --band-blue: #24429a;
    --photo-light: #c9d2dc;
    --photo-mid: #7d8ea6;
    --photo-dark: #27334d;
    --text-light: #ffffff;
  }
  * { margin: 0; padding: 0; box-sizing: border-box; }
  html, body {
    width: 1200px; height: 754px; overflow: hidden;
    background: var(--page);
  }
  .slide {
    position: absolute; left: 40px; top: 61px;
    width: 1120px; height: 632px;
    background: var(--panel-grey);
    overflow: hidden;
    box-shadow: 0 4px 14px rgba(0,0,0,0.18);
    font-family: "Montserrat", Arial, sans-serif;
  }
  .hero { position: absolute; left: 0; top: 0; width: 1120px; height: 477px; }
  .brand {
    position: absolute; left: 70px; top: 190px; width: 346px; height: 112px;
    display: flex; align-items: center; justify-content: center; gap: 16px;
  }
  .brand-dot {
    width: 22px; height: 22px; border-radius: 50%;
    background: var(--brand-green); flex: none;
  }
  .brand-name {
    font-size: 46px; font-weight: 500; color: var(--brand-blue);
    line-height: 1.12; letter-spacing: 0.5px;
  }
  .brand-name span { display: block; }
  .title-band {
    position: absolute; left: 0; top: 477px; width: 1120px; height: 126px;
    background: linear-gradient(to bottom, var(--green-top), var(--green-bottom));
    color: var(--text-light); text-align: center;
  }
  .title-band h1 {
    font-weight: 400; font-size: 38px; letter-spacing: 0.5px;
    margin-top: 16px; line-height: 1.1;
  }
  .title-band p {
    font-size: 14.5px; line-height: 1.45; margin: 10px auto 0; width: 1000px;
  }
  .base-band {
    position: absolute; left: 0; top: 603px; width: 1120px; height: 29px;
    background: var(--band-blue);
  }
</style>
</head>
<body>
  <div class="slide">
    <svg class="hero" width="1120" height="477" viewBox="0 0 1120 477">
      <defs>
        <linearGradient id="photoTone" x1="0" y1="0" x2="0" y2="1">
          <stop offset="0" stop-color="var(--photo-light)"/>
          <stop offset="0.45" stop-color="var(--photo-mid)"/>
          <stop offset="1" stop-color="var(--photo-dark)"/>
        </linearGradient>
      </defs>
      <rect x="408" y="0" width="712" height="477" fill="url(#photoTone)"
            role="img" aria-label="Photo of a smiling business team in suits standing in a bright office"/>
      <path d="M408 -2 A240 240 0 0 1 408 478" fill="none" stroke="var(--ring-white)" stroke-width="7"/>
      <path d="M408 73 A165 165 0 0 1 408 403 Z" fill="var(--inner-grey)"/>
    </svg>

    <div class="brand">
      <span class="brand-dot"></span>
      <div class="brand-name"><span>Lantern</span><span>Quorix</span></div>
    </div>

    <div class="title-band">
      <h1>PRESENTATION TITLE GOES HERE</h1>
      <p>Lorem Ipsum is simply dummy text of the printing and typesetting industry. Lorem Ipsum has been the industry's standard dummy text ever since the 1500s, when an unknown printer took a galley of type and scrambled it to make a type specimen book.</p>
    </div>
    <div class="base-band"></div>
  </div>
</body>
</html>
```